Brivane - Business Cards for a new venture

create business card for a startup classified business dealing in construction materials, the cards need to have a professional look but modern, more serious than playful, one of the samples must include the official font (attached), please explore using the official colors in the company's logo

Target Market(s)

Energy sector

Contact Information for Business Card

Font styles to use
Other font styles liked:
• suissnord

Requirements
Must have
• corporate colors (in logo attached)
Nice to have
• Official font (in one of the samples) font is : suissnord
Should not have
• Cartoonish look

```html
<!DOCTYPE html>
<html lang="en">
<head>
<meta charset="utf-8">
<title>Brivane – Business Card</title>
<link rel="stylesheet" href="https://fonts.googleapis.com/css2?family=Raleway:wght@400;500&display=swap">
<style>
  :root {
    --backdrop: #1f2233;
    --brand-blue: #0f4577;
    --ink-blue: #1d4f86;
    --rule-blue: #4a6c98;
    --steel-grey: #9a9ea4;
    --card-white: #ffffff;
  }
  * { margin: 0; padding: 0; box-sizing: border-box; }
  html, body {
    width: 1200px; height: 1200px; overflow: hidden;
    background: var(--backdrop);
    font-family: "Raleway", sans-serif;
  }
  .sheet {
    position: relative; width: 1200px; height: 1200px;
    display: flex; flex-direction: column; align-items: center;
    justify-content: center; gap: 80px;
  }
  .card {
    position: relative; width: 840px; height: 480px;
    border-radius: 44px; overflow: hidden;
  }
  .card--front {
    background: var(--brand-blue);
    display: flex; align-items: center; justify-content: center;
  }
  .front-wordmark {
    color: var(--card-white);
    font-weight: 500; font-size: 46px; letter-spacing: 14px;
    text-transform: uppercase; margin-top: 40px;
  }
  .card--back { background: var(--card-white); color: var(--ink-blue); }
  .back-wordmark {
    position: absolute; left: 200px; top: 96px; width: 300px;
    display: flex; align-items: center; justify-content: center; gap: 14px;
    color: var(--steel-grey); font-weight: 500; font-size: 30px;
    letter-spacing: 9px; text-transform: uppercase;
  }
  .back-wordmark .mark-dot {
    width: 18px; height: 18px; border-radius: 50%; background: var(--brand-blue);
  }
  .rule {
    position: absolute; height: 1.5px; background: var(--rule-blue);
  }
  .rule--upper { left: 90px; right: 60px; top: 196px; }
  .rule--lower { left: 150px; right: 0; top: 418px; }
  .person {
    position: absolute; left: 110px; top: 240px; text-align: right;
  }
  .person__name { font-size: 38px; font-weight: 400; line-height: 1.1; }
  .person__role { font-size: 20px; margin-top: 2px; }
  .contacts {
    position: absolute; left: 520px; top: 222px; list-style: none;
    font-size: 21px; line-height: 1;
  }
  .contacts li { display: flex; align-items: center; gap: 16px; height: 34px; }
  .contacts svg { width: 24px; height: 24px; fill: var(--ink-blue); flex: none; }
  .address {
    position: absolute; left: 0; right: 0; top: 372px;
    text-align: center; font-size: 19px; letter-spacing: 0.5px;
  }
</style>
</head>
<body>
<main class="sheet">
  <section class="card card--front" aria-label="Card front">
    <div class="front-wordmark">Brivane</div>
  </section>

  <section class="card card--back" aria-label="Card back">
    <div class="back-wordmark"><span class="mark-dot"></span><span>Brivane</span></div>
    <div class="rule rule--upper"></div>

    <div class="person">
      <div class="person__name">Name of Person</div>
      <div class="person__role">Designation</div>
    </div>

    <ul class="contacts">
      <li>
        <svg viewBox="0 0 24 24" aria-hidden="true"><path d="M3 8c0-2 4-4 9-4s9 2 9 4v2h-5V8.5c-1-.4-2.5-.6-4-.6s-3 .2-4 .6V10H3zM6 12h12l2 8H4zm6 2a2.5 2.5 0 1 0 0 5 2.5 2.5 0 0 0 0-5z"/></svg>
        <span>+ 123 456 789</span>
      </li>
      <li>
        <svg viewBox="0 0 24 24" aria-hidden="true"><path d="M12 2a10 10 0 1 1-5 18.7L2 22l1.4-4.8A10 10 0 0 1 12 2zm0 2a8 8 0 0 0-6.7 12.4l-.8 2.7 2.8-.8A8 8 0 1 0 12 4zm-3 3.5h1.8l1 2.6-1.2 1.2a6 6 0 0 0 2.6 2.6l1.2-1.2 2.6 1V16c0 .6-.5 1-1 1A8 8 0 0 1 8 9.5c0-.6.4-2 1-2z"/></svg>
        <span>+ 123 456 789</span>
      </li>
      <li>
        <svg viewBox="0 0 24 24" aria-hidden="true"><path d="M2 5h20v14H2zm2 2v.3l8 5.7 8-5.7V7zm0 2.7V17h16V9.7l-8 5.6z"/></svg>
        <span>name@email.com</span>
      </li>
    </ul>

    <div class="address">No.01, Adrs line 01, Adrs line 02, City, Country.</div>
    <div class="rule rule--lower"></div>
  </section>
</main>
</body>
</html>
```